Business Card Design for a Software Startup

We'd like to have a business card design. We already have a logo. Basically what we need is a clean design with name, address, cellphone and phone numbers, e-mail and web site address (front) and a space on the back with our logo with the company name on the right side and some texts on the bottom.
We are a development and consulting company in Brazil with highly qualified team of professionals in Java, iOS and Android development and consulting.

Target Market(s)

CIO, IT managers of mid to big size companies

Industry/Entity Type

Business

```html
<!DOCTYPE html>
<html lang="en">
<head>
<meta charset="utf-8">
<title>VOLTRA Business Card</title>
<link rel="stylesheet" href="https://fonts.googleapis.com/css2?family=Source+Sans+3:wght@400;600;700&display=swap">
<style>
  :root {
    --page: #ffffff;
    --card-black: #000000;
    --blue-bright: #00aeef;
    --blue-mid: #1a7fbf;
    --indigo: #423f6b;
    --wordmark: #2c4266;
    --mark: #1b79b8;
    --link: #1aa5e0;
    --white: #ffffff;
  }
  * { margin: 0; padding: 0; box-sizing: border-box; }
  html, body {
    width: 1200px; height: 849px; overflow: hidden;
    background: var(--page);
    font-family: "Source Sans 3", sans-serif;
  }
  .canvas { position: relative; width: 1200px; height: 849px; }

  .card { position: absolute; background: var(--card-black); overflow: hidden; }

  /* back side */
  .card--back { left: 222px; top: 47px; width: 646px; height: 353px; }
  .brand-lockup {
    position: absolute; left: 67px; top: 102px;
    display: flex; align-items: center; gap: 22px;
  }
  .brand-square {
    width: 102px; height: 102px; border-radius: 10px;
    background: var(--mark);
  }
  .brand-name {
    font-weight: 700; font-size: 96px; line-height: 1;
    color: var(--wordmark); letter-spacing: 2px;
  }
  .tagline-band {
    position: absolute; left: 0; bottom: 0; width: 100%; height: 54px;
    background: linear-gradient(90deg, var(--blue-bright), var(--blue-mid) 45%, var(--indigo));
    display: flex; align-items: center; justify-content: center;
  }
  .tagline { color: var(--white); font-size: 20px; padding-left: 12px; }

  /* front side */
  .card--front { left: 214px; top: 463px; width: 648px; height: 352px; border: 1px solid #1a6b99; }
  .front-brand {
    position: absolute; left: 0; top: 0; width: 318px; height: 100%;
  }
  .front-square {
    position: absolute; left: 78px; top: 67px;
    width: 166px; height: 166px; border-radius: 22px;
    background: var(--mark);
  }
  .front-name {
    position: absolute; left: 0; width: 100%; top: 238px; text-align: center;
    font-weight: 700; font-size: 48px; line-height: 1;
    color: var(--wordmark); letter-spacing: 1px;
  }
  .front-web {
    position: absolute; left: 0; width: 100%; top: 321px; text-align: center;
    font-size: 13px; color: var(--link);
  }
  .contact-panel {
    position: absolute; left: 318px; top: 0; right: 0; bottom: 0;
    background: linear-gradient(90deg, var(--blue-bright), var(--blue-mid) 40%, var(--indigo));
    color: var(--white);
  }
  .contact-panel p { position: absolute; left: 88px; white-space: nowrap; line-height: 1; }
  .person-name { top: 56px; font-size: 25px; }
  .person-role { top: 96px; font-size: 18px; }
  .contact-line { font-size: 16px; }
  .addr-1 { top: 161px; }
  .addr-2 { top: 184px; }
  .tel { top: 231px; }
  .cell { top: 255px; }
  .mail { top: 278px; }
</style>
</head>
<body>
<main class="canvas">
  <section class="card card--back" aria-label="Card back">
    <div class="brand-lockup">
      <span class="brand-square"></span>
      <span class="brand-name">VOLTRA</span>
    </div>
    <div class="tagline-band"><span class="tagline">IT Team Professional</span></div>
  </section>

  <section class="card card--front" aria-label="Card front">
    <div class="front-brand">
      <span class="front-square"></span>
      <span class="front-name">VOLTRA</span>
      <span class="front-web">www.voltra.com</span>
    </div>
    <div class="contact-panel">
      <p class="person-name">Mr. Someone</p>
      <p class="person-role">Director</p>
      <p class="contact-line addr-1">address somewhere</p>
      <p class="contact-line addr-2">Brazil</p>
      <p class="contact-line tel">tel:&nbsp;&nbsp; 1-555-214-3080</p>
      <p class="contact-line cell">cell: 1-555-730-6120</p>
      <p class="contact-line mail">information@voltra.com</p>
    </div>
  </section>
</main>
</body>
</html>
```